Consultant ot credit unions that operate a property and casualty insurance agency

Industry/Entity Type

Insurance

Contact Information for Business Card

Dorian Velcote
Credit Union Insurance Agency Consultant
dorianvelcote@mailbrook.example
562 318-4092
418 Tamsin Court
Long Beach, CA 90814

```html
<!DOCTYPE html>
<html lang="en">
<head>
<meta charset="utf-8">
<title>Dorian Velcote – Business Card</title>
<link href="https://fonts.googleapis.com/css2?family=Exo+2:wght@400;600&family=Oswald:wght@600&family=Days+One&display=swap" rel="stylesheet">
<style>
  :root {
    --backdrop: #8c8c8c;
    --card-white: #ffffff;
    --brand-orange: #f08a1c;
    --brand-orange-light: #f7a53a;
    --ink-dark: #1f1f1f;
    --panel-dark: #2a2a2a;
    --panel-darker: #1e1e1e;
    --text-light: #f2f2f2;
  }
  html, body {
    margin: 0;
    width: 1200px;
    height: 900px;
    overflow: hidden;
    background: var(--backdrop);
  }
  .business-card {
    position: absolute;
    left: 150px;
    top: 180px;
    width: 900px;
    height: 540px;
    border-radius: 36px;
    overflow: hidden;
    background: var(--card-white);
    box-shadow: 0 24px 50px rgba(0,0,0,0.35);
  }
  .identity {
    position: absolute;
    left: 0; top: 0;
    width: 100%;
    height: 282px;
  }
  .brand-square {
    position: absolute;
    left: 110px;
    top: 70px;
    width: 140px;
    height: 140px;
    border-radius: 18px;
    background: linear-gradient(180deg, var(--brand-orange-light), var(--brand-orange));
  }
  .person-name {
    position: absolute;
    left: 290px;
    top: 72px;
    margin: 0;
    font-family: "Days One", sans-serif;
    font-weight: 400;
    font-size: 72px;
    line-height: 1;
    color: var(--brand-orange);
  }
  .person-title {
    position: absolute;
    left: 292px;
    top: 166px;
    margin: 0;
    font-family: "Oswald", sans-serif;
    font-weight: 600;
    font-size: 29px;
    letter-spacing: 0.5px;
    color: var(--ink-dark);
    text-transform: uppercase;
  }
  .tagline-band {
    position: absolute;
    left: 0; top: 282px;
    width: 100%;
    height: 28px;
    background: linear-gradient(90deg, var(--brand-orange), var(--brand-orange-light));
    display: flex;
    align-items: center;
    justify-content: space-around;
    padding: 0 40px;
    box-sizing: border-box;
    font-family: "Exo 2", sans-serif;
    font-weight: 600;
    font-size: 19px;
    color: var(--ink-dark);
  }
  .contact-panel {
    position: absolute;
    left: 0; top: 310px;
    width: 100%;
    height: 230px;
    background: linear-gradient(180deg, var(--panel-dark), var(--panel-darker));
    text-align: center;
    font-family: "Exo 2", sans-serif;
  }
  .contact-phone {
    margin: 48px 0 4px;
    font-size: 40px;
    font-weight: 400;
    letter-spacing: 1px;
    color: var(--brand-orange);
  }
  .contact-email,
  .contact-address {
    margin: 0;
    font-size: 28px;
    color: var(--text-light);
    letter-spacing: 0.5px;
  }
  .contact-address { font-size: 31px; margin-top: 4px; }
</style>
</head>
<body>
  <div class="business-card">
    <header class="identity">
      <div class="brand-square" aria-hidden="true"></div>
      <h1 class="person-name">Dorian Velcote</h1>
      <p class="person-title">Credit Union Insurance Agency Consultant</p>
    </header>
    <div class="tagline-band" aria-label="Focused on you">
      <span>F</span><span>O</span><span>C</span><span>U</span><span>S</span><span>E</span><span>D</span>
      <span>&nbsp;</span><span>O</span><span>N</span><span>&nbsp;</span>
      <span>Y</span><span>O</span><span>U</span>
    </div>
    <section class="contact-panel">
      <p class="contact-phone">562 318-4092</p>
      <p class="contact-email">dorianvelcote@mailbrook.example</p>
      <p class="contact-address">418 Tamsin Court Long Beach, CA 90814</p>
    </section>
  </div>
</body>
</html>
```